Buchcover-Design für Science-Fiction-Roman
Zielgruppe
Ich habe einen Science-Fiction-Roman geschrieben und benötige dafür ein Buchcover.
Meine Zielgruppe sind Leser- und Leserinnen ab 18, Science-Fiction-Fans.
Aufgabenstellung
Zur Einstimmung und Orientierung habe ich ein kurzes Exposé und eine Leseprobe des Romans hochgeladen.
Für das Cover stelle ich mir etwas Dezentes aber trotzdem künstlerisch Anspruchsvolles vor, gerne auch abstrakt.
Es sollte der Titel (Unter Glas), meine Name (Lenor Vasić) und 'Roman' auf dem Cover.
Den genauen Klappentext reiche ich noch nach.
Das Format ist 12,7 x 20,32 cm (5 x 8 Zoll), Rückenbreite etwa 2 cm.

```html
<!DOCTYPE html>
<html lang="de">
<head>
<meta charset="utf-8">
<title>Unter Glas – Buchumschlag</title>
<link href="https://fonts.googleapis.com/css2?family=Bebas+Neue&family=Barlow:wght@400;500&display=swap" rel="stylesheet">
<style>
  :root {
    --paper: #ffffff;
    --rust-top: #a8351f;
    --orange-mid: #d4530f;
    --orange-low: #e07a35;
    --peach: #f6b48c;
    --spine-band: #e0814a;
    --ink-dark: #5a2410;
    --white: #ffffff;
  }
  * { margin: 0; padding: 0; box-sizing: border-box; }
  html, body { width: 1200px; height: 889px; overflow: hidden; background: var(--paper); }
  .jacket { position: relative; width: 1200px; height: 889px; }

  .panel {
    position: absolute; top: 32px; height: 820px; overflow: hidden;
    background: linear-gradient(180deg, var(--rust-top) 0%, var(--orange-mid) 35%, var(--orange-low) 70%, #d86a2c 100%);
  }
  .back-cover { left: 47px; width: 512px; }
  .spine { left: 560px; width: 80px; outline: 1px solid var(--paper); }
  .front-cover { left: 641px; width: 512px; }

  .artwork { position: absolute; }
  .back-artwork {
    left: 0; top: 520px; width: 512px; height: 300px;
    background: radial-gradient(ellipse at 20% 90%, rgba(120,40,20,0.55), rgba(200,90,40,0) 70%);
  }
  .front-artwork-clock {
    right: 0; top: 0; width: 260px; height: 360px;
    background: radial-gradient(ellipse at 90% 10%, rgba(110,30,20,0.55), rgba(160,50,20,0) 70%);
  }
  .front-artwork-skyline {
    left: 0; top: 420px; width: 512px; height: 400px;
    background: linear-gradient(180deg, rgba(180,60,30,0) 0%, rgba(170,55,30,0.45) 45%, rgba(150,45,25,0.6) 100%);
  }
  .title-strip {
    position: absolute; left: 148px; top: 320px; width: 212px; height: 500px;
    background: rgba(240,150,90,0.25);
  }
  .front-figure {
    position: absolute; left: 364px; top: 250px; width: 80px; height: 180px;
    border-radius: 40px;
    background: radial-gradient(ellipse, rgba(74,22,48,0.55), rgba(74,22,48,0) 70%);
  }
  .spine-figure {
    position: absolute; left: 2px; top: 250px; width: 76px; height: 180px;
    border-radius: 38px;
    background: radial-gradient(ellipse, rgba(74,22,48,0.5), rgba(74,22,48,0) 70%);
  }

  .display { font-family: "Bebas Neue", "Anton", sans-serif; line-height: 1; font-weight: 400; }
  .body-font { font-family: "Barlow", "Helvetica Neue", sans-serif; }

  /* back */
  .back-title { position: absolute; left: 39px; top: 40px; }
  .back-title .line-one { color: var(--peach); font-size: 118px; display: block; height: 100px; }
  .back-title .line-two { color: var(--white); font-size: 118px; display: block; }
  .blurb {
    position: absolute; left: 39px; top: 246px; width: 430px;
    color: var(--white); font-size: 15px; line-height: 18.9px; font-weight: 400;
  }
  .code-field {
    position: absolute; left: 271px; top: 663px; width: 202px; height: 122px;
    background: var(--paper);
  }

  /* spine */
  .spine-band { position: absolute; left: 0; top: 470px; width: 80px; height: 350px; background: var(--spine-band); }
  .spine-title, .spine-author {
    position: absolute; writing-mode: vertical-rl; transform: rotate(180deg);
    font-family: "Barlow", "Helvetica Neue", sans-serif; font-weight: 500; white-space: nowrap;
  }
  .spine-title { left: 26px; top: 36px; height: 200px; width: 30px; text-align: end; color: var(--white); font-size: 27px; letter-spacing: 1px; }
  .spine-author { left: 24px; top: 560px; height: 260px; width: 32px; text-align: start; color: var(--ink-dark); font-size: 27px; padding-top: 32px; }

  /* front */
  .front-author {
    position: absolute; left: 177px; top: 52px;
    color: var(--white); font-size: 28px; font-weight: 500;
  }
  .front-title { position: absolute; left: 0; top: 0; }
  .front-title-top {
    position: absolute; left: 177px; top: 96px; width: 162px; height: 140px; overflow: visible;
  }
  .front-title-top text { fill: var(--peach); font-family: "Bebas Neue", "Anton", sans-serif; }
  .front-title-vertical {
    position: absolute; left: 177px; top: 283px; width: 163px; height: 524px;
    writing-mode: vertical-rl; color: var(--white);
    font-size: 233px; line-height: 163px; letter-spacing: 26px; overflow: hidden;
  }
  .genre {
    position: absolute; left: 177px; top: 784px;
    color: var(--ink-dark); font-size: 14.5px; letter-spacing: 0.3px;
  }
</style>
</head>
<body>
<div class="jacket">

  <section class="panel back-cover">
    <div class="artwork back-artwork" role="img" aria-label="Illustration einer großen Uhr mit römischen Ziffern und Zahnrädern in Orangetönen"></div>
    <h2 class="back-title display"><span class="line-one">Unter</span><span class="line-two">Glas</span></h2>
    <p class="blurb body-font">Lorem ipsum dolor sit amet, consectetuer adipiscing elit. Aenean commodo ligula eget dolor. Aenean massa. Cum sociis natoque penatibus et magnis dis parturient montes, nascetur ridiculus mus. Donec quam felis, ultricies nec, pellentesque eu, pretium quis, sem. Nulla consequat massa quis enim. Donec pede justo, fringilla vel, aliquet nec, vulputate eget, arcu. In enim justo, rhoncus ut, imperdiet a, venenatis vitae, justo. Nullam dictum felis eu pede mollis pretium. Integer tincidunt. Cras dapibus. Vivamus elementum semper nisi. Aenean vulputate eleifend tellus. Aenean leo ligula, porttitor eu, consequat vitae, eleifend ac, enim. Aliquam lorem ante, dapibus in, viverra quis, feugiat a, tellus.</p>
    <div class="code-field"></div>
  </section>

  <section class="panel spine">
    <div class="spine-band"></div>
    <div class="spine-figure" role="img" aria-label="Silhouette einer fallenden Person"></div>
    <div class="spine-title">UNTER GLAS</div>
    <div class="spine-author">Lenor Vasić</div>
  </section>

  <section class="panel front-cover">
    <div class="artwork front-artwork-clock" role="img" aria-label="Ausschnitt einer Uhr mit Zahnrädern in dunklem Rostrot"></div>
    <div class="artwork front-artwork-skyline" role="img" aria-label="Stilisierte Hochhaus-Skyline im orangefarbenen Dunst"></div>
    <div class="title-strip"></div>
    <div class="front-figure" role="img" aria-label="Silhouette einer kopfüber fallenden Person"></div>
    <p class="front-author body-font">Lenor Vasić</p>
    <h1 class="front-title">
      <svg class="front-title-top" viewBox="0 0 162 140" aria-label="UNTER">
        <text x="0" y="139" font-size="199" textLength="162" lengthAdjust="spacingAndGlyphs">UNTER</text>
      </svg>
      <span class="front-title-vertical display">GLAS</span>
    </h1>
    <p class="genre body-font">Science Fiction Roman</p>
  </section>

</div>
</body>
</html>
```